One of Australia's fastest growing energy maintenance contractors needs a new website

www.panelbrite.com.au
Our business has evolved over the past years and now our website is no longer relevant.
We clean solar panels and we vacuum roof gutters.
We clean solar panels on the roofs of residential houses right up to billion dollar solar farms with in excess of 1 million panels. We offer thermal image testing and bird proofing for our residential and commercial clients and thermal drone imaging services for our solar farm clients.
We vacuum clean roof gutters (using a LoftSuk) on the residential house next door right up to enormous private and public schools, colleges, shopping centres, strat complexes and commercial buildings.
When first built our business had more of a domestic residential skew and the website reflected that. While that is still part of our core business we are now bidding on and have secured large government, commercial and infrastructure contracts and our new website needs to reflect our growth and our new business. We need a new site that it optimised for both desktop ad phone viewing as our latest figures showed that 73% of people visiting our site are on mobile phones. We have an extensive amount of data on Trekmetrics available as well as Bidlinks. Both that would also need integrating with the site along with a few other plugins such as Kembo Chat IQ, Friendwall etc along with SEO key words etc. We are also the winner and finalists over multiple years of the small business of the year awards and we like to proudly and prominently display those on our site.
We are looking for a new site with a modern professional feel / theme
There is a definitive break in our business between the solar Panel cleaning clients and the gutter cleaning clients so we would like a home page that begins with a simple choice:
Solar Panel Cleaning – Gutter Cleaning
With a professional full screen background image (we have hundreds to choose from) and along the bottom a small area with rights reserved etc, phone number etc (at some point in the future we will split these into two businesses but for now it’s what we have).
After that selection is made we would like a repeat of that same scenario but the selection is:
If it’s Solar Panel Cleaning
(new background image)
Government – Infrastructure – Commercial – Residential
If it’s Gutter Cleaning
(new background image)
Government – Strata – Commercial – Residential
After making those choices then onto the relevant pages with background images relevant to each sector and a them that suits (on the residential we would like to keep the link to our trekmetrics reviews) - We will provide copy / text for each relevant page.
Other than that, a menu inclusive of the above and:
Resellers Portal – we will provide a link to this from Kembo CRM)
Customer portal (we will supply a link to this from our booking system)
We also need a page for our Solar Resellers / Partners page but we will give them a link to this, it won’t be listed on the site.
Request a quote page (Again we will provide information from Kembo as this will be linked to the CRM)
Standard contact us page inclusive of phone numbers, address and fields supplied from CRM
Sydney – 02 7391 5084
Southern Highlands – 02 4863 1507
Goulburn – 02 4863 1507
Canberra – 02 6178 3045
Wollongong – 02 4239 7615
sales@panelbrite.com.au
Head Office - Ferndell NSW 2583
ABN: 48762093115
Responsive Design: Optimized for desktop and mobile (73% mobile visitors).
Fast Loading Speed: Optimized for performance.
Smooth Transition Animations: For service and category selection.
Sticky Contact Bar: Always accessible at the bottom of mobile screens for quick calls.
SEO Optimization: Focused on government tenders, large-scale commercial contracts, and infrastructure projects.
Integrations
Trekmetrics & Trekmetrics Bidlinks.
Kembo Chat IQ.
Friendwall Beacon.
SEO tools and keyword optimization.
Many many more images available if needed

```html
<!DOCTYPE html>
<html lang="en">
<head>
<meta charset="utf-8">
<title>PanelBrite – Gutter Cleaning</title>
<link href="https://fonts.googleapis.com/css2?family=Poppins:wght@300;400;500;600;700&display=swap" rel="stylesheet">
<style>
:root{
  --blue:#17a3d8;
  --blue-btn:#1d8fd0;
  --orange:#f7a21b;
  --ink:#1d1d1f;
  --text:#4a4a4a;
  --grey:#f1f1f1;
  --line:#e4e4e4;
  --white:#ffffff;
  --badge:#d7dcd8;
}
*{box-sizing:border-box;margin:0;padding:0}
html,body{width:1200px;height:4658px;overflow:hidden}
body{font-family:'Poppins',sans-serif;color:var(--text);background:var(--white);position:relative}
section,header,footer{position:absolute;left:0;width:1200px}

/* header */
.site-header{top:0;height:74px;background:var(--white);box-shadow:0 1px 4px rgba(0,0,0,.06)}
.brand{position:absolute;display:flex;align-items:center;gap:8px;font-weight:600;color:var(--blue)}
.brand .dot{border-radius:50%;background:var(--blue)}
.site-header .brand{left:164px;top:20px;font-size:20px}
.site-header .brand .dot{width:30px;height:30px}
.nav{position:absolute;right:166px;top:20px;display:flex;align-items:center;gap:19px;font-size:12px;color:var(--ink);font-weight:500}
.nav .quote{background:var(--orange);color:var(--ink);border-radius:18px;padding:8px 18px;font-size:11px}

/* hero */
.hero{top:74px;height:329px;background:linear-gradient(135deg,#3b3a36 0%,#6f6a60 45%,#2a2926 100%)}
.hero h1{position:absolute;width:100%;text-align:center;top:128px;color:var(--white);font-size:47px;font-weight:600}

/* intro */
.intro{top:403px;height:560px}
.intro h2{position:absolute;width:100%;text-align:center;top:68px;font-size:40px;font-weight:600;color:var(--ink)}
.intro p{position:absolute;left:300px;width:600px;top:144px;text-align:center;font-size:12.5px;line-height:24px}
.sector{position:absolute;top:260px;width:211px;height:251px;color:var(--white);padding:28px 24px}
.sector h3{font-size:15px;font-weight:600;letter-spacing:.3px}
.sector .rule{width:30px;height:2px;background:var(--orange);margin:10px 0 18px}
.sector p{font-size:12px;line-height:22px;color:var(--white)}
.sector a{font-size:11px;color:var(--orange);text-decoration:underline;display:block;margin-top:8px}
.s1{left:164px;background:linear-gradient(180deg,#3b4048,#5a5145 60%,#2e2a24)}
.s2{left:385px;background:linear-gradient(180deg,#3c424b,#6d7077 60%,#47494d)}
.s3{left:605px;background:linear-gradient(180deg,#353b45,#4e4538 60%,#2a2520)}
.s4{left:824px;background:linear-gradient(180deg,#3a414b,#6b5b48 60%,#3a3128)}

/* reviews */
.reviews{top:988px;height:230px}
.rev-head{position:absolute;left:157px;width:885px;top:0;height:42px;border:1px solid var(--line);display:flex;align-items:center;padding:0 14px;font-size:11px;color:var(--ink);gap:8px}
.rev-head .name{color:#4a7bd6;font-weight:500;font-size:13px}
.stars{color:#f6b400;letter-spacing:1px}
.rev-head .write{margin-left:auto;background:#3f7de0;color:var(--white);font-size:9px;padding:6px 12px;border-radius:3px}
.rev{position:absolute;top:53px;width:214px;height:162px;border:1px solid var(--line);box-shadow:0 1px 3px rgba(0,0,0,.06);padding:14px 13px;font-size:10px;line-height:15px;color:var(--ink)}
.rev .who{display:flex;gap:10px;align-items:center;margin-bottom:8px}
.rev .av{width:28px;height:28px;border-radius:50%;background:#9aa3a9}
.rev .nm{font-weight:600;font-size:10px}
.rev .dt{font-size:8px;color:#999;line-height:11px}
.rev .src{position:absolute;right:12px;top:14px;width:10px;height:10px;border-radius:50%;background:#c9c9c9}
.rev .stars{font-size:11px;display:block;margin-bottom:4px}
.rev .more{color:#999;font-size:9px}
.arrow{position:absolute;top:125px;font-size:18px;color:#aaa}

/* roof + checklist */
.roof{top:1276px;height:320px;background:linear-gradient(180deg,#f3f4f2 0%,#cfd3d2 40%,#6c7b72 75%,#3a463e 100%)}
.why{top:1596px;height:466px}
.why .panel{position:absolute;left:504px;top:0;width:696px;height:466px;background:var(--grey)}
.video{position:absolute;left:0;top:0;width:575px;height:325px;background:linear-gradient(120deg,#5f9a3a 0%,#3a6fb0 45%,#1f2c3a 100%);box-shadow:0 4px 10px rgba(0,0,0,.2)}
.video .bar{position:absolute;left:0;bottom:0;width:100%;height:16px;background:rgba(0,0,0,.7)}
.checks{position:absolute;left:656px;top:110px;list-style:none}
.checks li{display:flex;align-items:center;gap:18px;font-size:13px;color:var(--ink);height:42px}
.btn{display:inline-block;background:var(--blue-btn);color:var(--white);font-size:11px;font-weight:600;border-radius:18px;padding:9px 22px}
.why .btn{position:absolute;left:658px;top:374px}

/* gutter info */
.info{top:2156px;height:538px}
.info .strip{position:absolute;left:0;top:0;width:103px;height:538px;background:var(--grey)}
.info h2{position:absolute;left:162px;top:0;font-size:30px;font-weight:600;color:var(--ink)}
.info .copy{position:absolute;left:163px;top:60px;width:460px;font-size:11.2px;line-height:24px}
.info .copy p{margin-bottom:11px}
.info .photo{position:absolute;left:661px;top:0;width:539px;height:538px;background:linear-gradient(180deg,#7c5a4a 0%,#9aa3a0 35%,#6f7a74 70%,#4c5a50 100%)}
.info .badge{position:absolute;right:18px;bottom:18px;width:96px;height:96px;border-radius:50%;background:var(--badge)}

/* bushfire */
.bushfire{top:2783px;height:958px;background:var(--blue);color:var(--white)}
.bushfire h2{position:absolute;width:100%;text-align:center;top:46px;font-size:30px;font-weight:600}
.bushfire .photo{position:absolute;left:219px;top:132px;width:762px;height:426px;background:linear-gradient(135deg,#6d6a68 0%,#a9754c 40%,#e0783a 55%,#595654 100%)}
.bushfire .copy{position:absolute;left:219px;top:600px;width:762px;font-size:11.2px;line-height:24px}
.bushfire .copy p{margin-bottom:11px}

/* complete service */
.service{top:3825px;height:393px}
.service .card{position:absolute;left:164px;top:0;width:472px;height:393px;background:var(--grey)}
.service h2{position:absolute;left:232px;top:64px;font-size:30px;font-weight:600;color:var(--ink)}
.service .copy{position:absolute;left:232px;top:128px;width:330px;font-size:11.5px;line-height:24px;color:var(--ink)}
.service .copy p{margin-bottom:10px}
.service .btn{position:absolute;left:234px;top:228px}
.service .tag{position:absolute;left:232px;top:306px;width:200px;font-weight:600;color:var(--ink);font-size:20px;line-height:24px}
.service .photo{position:absolute;left:636px;top:0;width:399px;height:393px;background:linear-gradient(180deg,#eaf1ef 0%,#6b5242 35%,#3e4e3a 70%,#7f8d6a 100%)}

/* footer */
.site-footer{top:4302px;height:356px;background:var(--blue);color:var(--white)}
.site-footer .brand{left:164px;top:48px;font-size:22px;color:var(--white);font-weight:500}
.site-footer .brand .dot{width:34px;height:34px;background:var(--white)}
.about{position:absolute;left:164px;top:104px;width:210px;font-size:10.5px;line-height:20px}
.social{position:absolute;left:166px;top:168px;display:flex;gap:10px}
.social span{width:28px;height:28px;border-radius:50%;background:var(--white)}
.col{position:absolute;top:62px;font-size:10.5px;line-height:29px}
.col h4{font-size:11px;font-weight:600;margin-bottom:10px;line-height:16px}
.col li{list-style:none;display:flex;align-items:center;gap:8px}
.links{left:430px}
.contact{left:605px}
.touch{left:867px}
.touch li{align-items:flex-start;line-height:20px;margin-bottom:8px}
.touch svg{margin-top:5px;flex:none}
.copyright{position:absolute;width:100%;text-align:center;top:324px;font-size:9px}
</style>
</head>
<body>

<header class="site-header">
  <div class="brand"><span class="dot"></span>PanelBrite</div>
  <nav class="nav">
    <span>SOLAR CLEANING</span><span>GUTTER CLEANING</span><span>AERODUST</span><span>CONTACT</span><span class="quote">GET A QUOTE</span>
  </nav>
</header>

<section class="hero" role="img" aria-label="House eaves and roof gutter photo">
  <h1>Gutter Cleaning</h1>
</section>

<section class="intro">
  <h2>Title Lorem Ipsum</h2>
  <p>Lorem ipsum dolor sit amet, consectetur adipiscing elit, sed do eiusmod tempor incididunt ut labore et dolore magna aliqua. Quis ipsum suspendisse ultrices gravida. Risus commodo viverra maecenas accumsan lacus vel facilisis.</p>
  <div class="sector s1" role="img" aria-label="Government building photo"><h3>GOVERNMENT</h3><div class="rule"></div><p>Risus commodo viverra ma ecenas lacus velfacil.</p><a>Learn More</a></div>
  <div class="sector s2" role="img" aria-label="Industrial metal roof photo"><h3>INFRASTRUCTURE</h3><div class="rule"></div><p>Risus commodo viverra ma ecenas lacus velfacil.</p><a>Learn More</a></div>
  <div class="sector s3" role="img" aria-label="Commercial building photo"><h3>COMMERCIAL</h3><div class="rule"></div><p>Risus commodo viverra ma ecenas lacus velfacil.</p><a>Learn More</a></div>
  <div class="sector s4" role="img" aria-label="Residential house photo"><h3>RESIDENTIAL</h3><div class="rule"></div><p>Risus commodo viverra ma ecenas lacus velfacil.</p><a>Learn More</a></div>
</section>

<section class="reviews">
  <div class="rev-head"><span class="name">Trekmetrics</span><b>Excellent</b><span class="stars">★★★★★</span><b>4.9</b> | <b>392 reviews</b><span class="write">Write a review</span></div>
  <span class="arrow" style="left:140px">‹</span>
  <div class="rev" style="left:157px"><span class="src"></span><div class="who"><span class="av"></span><div><div class="nm">Marlo Vance</div><div class="dt">14 February 2025</div></div></div><span class="stars">★★★★★</span>Great service</div>
  <div class="rev" style="left:381px"><span class="src"></span><div class="who"><span class="av"></span><div><div class="nm">Helena Pritchard</div><div class="dt">10 February 2025</div></div></div><span class="stars">★★★★★</span>Superb gutter clean (removed 50 Lts or grass weeds and leaves) and solar panel clean and test for dead cells and hot spots. Vey professional and…<br><span class="more">Read more</span></div>
  <div class="rev" style="left:605px"><span class="src"></span><div class="who"><span class="av" style="background:#2f7a3a"></span><div><div class="nm">Ross and Nadia Keel</div><div class="dt">7 February 2025</div></div></div><span class="stars">★★★★★</span>Excellent!<br>Arrived on time and did a great job again!</div>
  <div class="rev" style="left:829px"><span class="src"></span><div class="who"><span class="av" style="background:#555"></span><div><div class="nm">Odette Ramsey</div><div class="dt">7 February 2025</div></div></div><span class="stars">★★★★★</span>Reliable ! pleasant staff and love the reminder system and reasonable fees. Thankyou.</div>
  <span class="arrow" style="left:1048px">›</span>
</section>

<section class="roof" role="img" aria-label="Roof gable and gutter photo"></section>

<section class="why">
  <div class="panel"></div>
  <div class="video" role="img" aria-label="Video of gutter vacuum pole on a metal roof"><div class="bar"></div></div>
  <ul class="checks">
    <li><svg width="12" height="10" viewBox="0 0 12 10"><path d="M1 5l3.5 3.5L11 1" fill="none" stroke="#1d8fd0" stroke-width="1.6"/></svg>WE DON'T CLIMB ON YOUR ROOF</li>
    <li><svg width="12" height="10" viewBox="0 0 12 10"><path d="M1 5l3.5 3.5L11 1" fill="none" stroke="#1d8fd0" stroke-width="1.6"/></svg>WE DON'T SCRATCH YOUR GUTTERS</li>
    <li><svg width="12" height="10" viewBox="0 0 12 10"><path d="M1 5l3.5 3.5L11 1" fill="none" stroke="#1d8fd0" stroke-width="1.6"/></svg>WE DON'T TRASH YOUR GARDENS</li>
    <li><svg width="12" height="10" viewBox="0 0 12 10"><path d="M1 5l3.5 3.5L11 1" fill="none" stroke="#1d8fd0" stroke-width="1.6"/></svg>NO MESS NO FUSS</li>
    <li><svg width="12" height="10" viewBox="0 0 12 10"><path d="M1 5l3.5 3.5L11 1" fill="none" stroke="#1d8fd0" stroke-width="1.6"/></svg>FIXED PRICE QUOTES</li>
    <li><svg width="12" height="10" viewBox="0 0 12 10"><path d="M1 5l3.5 3.5L11 1" fill="none" stroke="#1d8fd0" stroke-width="1.6"/></svg>NO LEAF LEFT BEHIND!</li>
  </ul>
  <span class="btn">REQUEST A QUOTE</span>
</section>

<section class="info">
  <div class="strip"></div>
  <h2>Gutter Cleaning</h2>
  <div class="copy">
    <p>Blocked gutters may appear insignificant, but ensuring their proper functioning brings numerous benefits to your home.</p>
    <p>Gutters play a crucial role in managing the flow of rainwater away from your house during storms or heavy downpours. When they become blocked, water can accumulate in the wrong places and even seep back into your home, causing damage to both the interior and exterior.</p>
    <p>Therefore, it is essential to regularly maintain your gutters by removing leaves, sticks, and other debris.</p>
    <p>While it is advisable to clean out your gutters on a regular basis, springtime is particularly important for this task. Throughout autumn and winter, gutters tend to accumulate leaves and debris, and if they are not cleared before the arrival of spring and summer storms, the uncontrolled water flow can wreak havoc on your home.</p>
    <p>As water descends into your gutters, if they are clogged with debris it will cascade back towards your house, infiltrating your eaves and eventually seeping into your wall cavities, resulting in extensive damage.</p>
    <p>Roof damage and water infiltration can have devastating consequences for your home. Cleaning them is simple and cost effective.</p>
  </div>
  <div class="photo" role="img" aria-label="Worker vacuuming a house gutter from the ground, captioned We don't walk on the roof"><span class="badge" role="img" aria-label="Awards finalist badge"></span></div>
</section>

<section class="bushfire">
  <h2>Bushfire Preparation</h2>
  <div class="photo" role="img" aria-label="Dry leaves burning in a roof gutter"></div>
  <div class="copy">
    <p>Bushfire Prep</p>
    <p>Pine needles, leaves, twigs, and other dry debris lying in a gutter can easily serve as fuel for a fire caused by a few floating embers. These embers not only can drift up to a kilometre from a fire, but they are also more apt to ignite in the semi-enclosed area of a gutter. That's why it is pivotal for homeowners to keep their gutters clean during the hot and dry seasons.</p>
    <p>Unlike storms and other weather events, bushfires can form without much warning. That's why it's important to take proactive, protective measures to safeguard your home from damaging embers and flames. It could mean the difference between your home surviving or not.</p>
    <p>Blocked gutters can cause the water to run down your walls, this can result in staining on the walls, damp and, if left for an extended period of time a blocked gutter can also lead to more sinister structural problems.</p>
    <p>Having your gutters cleared annually is recommended by most home insurance providers and as with many home maintenance tasks, prevention is cheaper than fixing the damage caused when gutters are neglected.</p>
  </div>
</section>

<section class="service">
  <div class="card"></div>
  <h2>Complete Service</h2>
  <div class="copy">
    <p>It just makes sense! Get the full treatment and have peace of mind this Summer season.</p>
    <p>Book an obligation free over the phone quote</p>
  </div>
  <span class="btn">REQUEST A QUOTE</span>
  <div class="tag">No Leaf Left Behind</div>
  <div class="photo" role="img" aria-label="Worker cleaning the gutters of a commercial building with a vacuum pole"></div>
</section>

<footer class="site-footer">
  <div class="brand"><span class="dot"></span>PanelBrite</div>
  <p class="about">Lorem ipsum dolor amet, consectetur adipiscing elit, sed do eiusmod tempor incidi dunt ut</p>
  <div class="social"><span></span><span></span><span></span></div>
  <div class="col links"><h4>QUICK LINKS</h4><ul>
    <li>› Solar Cleaning</li><li>› Gutter Cleaning</li><li>› AeroDust</li><li>› Contact</li><li>› Resellers Portal</li><li>› Customer portal</li></ul></div>
  <div class="col contact"><h4>CONTACT</h4><ul>
    <li>Sydney – 02 7391 5084</li><li>Southern Highlands – 02 4863 1507</li><li>Goulburn – 02 4863 1507</li><li>Canberra – 02 6178 3045</li><li>Wollongong – 02 4239 7615</li></ul></div>
  <div class="col touch"><h4>GET IN TOUCH</h4><ul>
    <li><svg width="10" height="10" viewBox="0 0 10 10"><path d="M1 5L9 1 6 9 5 6z" fill="#fff"/></svg>sales@panelbrite.com.au</li>
    <li><svg width="10" height="12" viewBox="0 0 10 12"><path d="M5 11C2 7 1 5.5 1 4a4 4 0 018 0c0 1.5-1 3-4 7z" fill="#fff"/></svg><span>Head Office<br>Ferndell NSW 2583</span></li>
    <li><svg width="10" height="11" viewBox="0 0 10 11"><rect x="1" y="1" width="8" height="9" fill="none" stroke="#fff" stroke-width="1.2"/><path d="M3 4h4M3 6h4" stroke="#fff"/></svg>ABN: 48762093115</li></ul></div>
  <p class="copyright">© PanelBrite 2025</p>
</footer>

</body>
</html>
```